Our private family owned investment company owns a vineyard in Napa. We want to design a label to put on our wine bottles once wine is ready. We would like artists to develop a creative design for a new label using this wording: Vineyard 48172. The dimensions of the label will be the standard label size on a 750 ml wine bottle. We appreciate creative flair, a classy look, preferably color but open to black and white too; maybe submit both ways. **As more explanation for designers, our family founded and owned a business for over 50 years and our logo was a teal colored snowflake (see attached jpeg logo). Our first plant address was numbered 48172. After our business was sold, our new family office is on located at 48172 Dunmore. We have created a new business logo (see attached blue TRB logo) So the 48172 and 2 logos all have lineage and sentimental value to our family. Thank you for providing your unique creativity to this project.

Target Market(s)

to inspire conversation and reminiscing among friends and business associates when entertaining them.

Industry/Entity Type

Investment

Colors

Designer to choose colors to be used in the design.

Requirements
Must have
• Must Incorporate the wording: Vineyard 48172 - as part of the entire design and please see the attached logos (sketch of Vineyard 48172, blue snowflake logo, and TRB logo) and use any of these as a base, or part of, your new design. ** See project description for more detail on the meaning behind these logos.**

```html
<!DOCTYPE html>
<html lang="en">
<head>
<meta charset="utf-8">
<title>Vineyard 48172 — Wine Label</title>
<link rel="stylesheet" href="https://fonts.googleapis.com/css2?family=Cormorant+Garamond:wght@500&family=Marcellus&display=swap">
<style>
  :root {
    --backdrop: #111111;
    --label-edge: #141414;
    --gold-bright: #f2c230;
    --gold-deep: #b9860f;
    --ink: #0d0d0d;
    --napa-gold: #e6a51c;
  }
  html, body {
    margin: 0;
    padding: 0;
    width: 1200px;
    height: 1200px;
    overflow: hidden;
    background: var(--backdrop);
  }
  .canvas {
    width: 1200px;
    height: 1200px;
    display: flex;
    align-items: center;
    justify-content: center;
  }
  .wine-label { display: block; }
  .label-number {
    font-family: "Cormorant Garamond", serif;
    font-weight: 500;
    font-size: 170px;
    fill: var(--ink);
    letter-spacing: 8px;
  }
  .label-title {
    font-family: "Marcellus", serif;
    font-size: 96px;
    fill: var(--ink);
    letter-spacing: 10px;
  }
  .label-region {
    font-family: "Marcellus", serif;
    font-size: 50px;
    fill: var(--napa-gold);
    letter-spacing: 6px;
  }
</style>
</head>
<body>
<main class="canvas">
  <svg class="wine-label" width="780" height="980" viewBox="0 0 780 980" xmlns="http://www.w3.org/2000/svg">
    <defs>
      <linearGradient id="landscape-tones" x1="0" y1="0" x2="0" y2="1">
        <stop offset="0" stop-color="#e59a12"/>
        <stop offset="0.14" stop-color="#f3c766"/>
        <stop offset="0.3" stop-color="#fbf1d8"/>
        <stop offset="0.42" stop-color="#d9b77a"/>
        <stop offset="0.5" stop-color="#7c8e3c"/>
        <stop offset="0.56" stop-color="#9bb04a"/>
        <stop offset="0.7" stop-color="#5f8f2a"/>
        <stop offset="0.86" stop-color="#3f7019"/>
        <stop offset="1" stop-color="#1f3f0c"/>
      </linearGradient>
      <linearGradient id="gold-band" x1="0" y1="0" x2="0" y2="1">
        <stop offset="0" stop-color="#c9920f" stop-opacity="0.85"/>
        <stop offset="0.5" stop-color="#f4c12e" stop-opacity="0.95"/>
        <stop offset="1" stop-color="#c08a0c" stop-opacity="0.85"/>
      </linearGradient>
      <clipPath id="label-window">
        <polygon points="70,40 710,40 742,110 742,915 710,945 70,945 38,915 38,110"/>
      </clipPath>
    </defs>

    <polygon class="label-edge" points="60,0 720,0 780,100 780,930 740,980 40,980 0,930 0,100" fill="var(--label-edge)"/>

    <g clip-path="url(#label-window)">
      <rect class="label-landscape" x="30" y="30" width="720" height="925" fill="url(#landscape-tones)" role="img" aria-label="Sunlit Napa vineyard landscape with rows of vines under a golden sky"/>
      <path class="title-band" d="M30,500 Q390,530 750,500 L750,620 Q390,650 30,620 Z" fill="url(#gold-band)"/>
    </g>

    <polygon class="frame-outer" points="70,40 710,40 742,110 742,915 710,945 70,945 38,915 38,110" fill="none" stroke="var(--gold-bright)" stroke-width="6"/>
    <polygon class="frame-inner" points="78,54 702,54 728,114 728,908 702,931 78,931 52,908 52,114" fill="none" stroke="var(--gold-deep)" stroke-width="3"/>

    <text class="label-number" x="390" y="395" text-anchor="middle">48172</text>
    <text class="label-title" x="390" y="595" text-anchor="middle">VINEYARD</text>
    <text class="label-region" x="390" y="720" text-anchor="middle">NAPA</text>
  </svg>
</main>
</body>
</html>
```